Professional Letterhead for electronic use

I would like to inquire, if you could help me to create a letterhead, mostly for electronic use. Preferably in word file, with fixed letterhead design (header and footer), but will allow to add text on the main body of the letter. I usually operate online and would like to be able to add text, convert it to PDF and send as an attachment.
Target Market(s)
High net worth clients.
Industry/Entity Type
Real Estate Agent
Font styles to use
Other font styles liked:
- Century Gothic
Requirements
Must have
- Company name, logo, full address, email address, landline number, website address, Homestead Adjudicator logo, PELV logo, Company registration number
Nice to have
- Professional and elegant design

```html
<!DOCTYPE html>
<html lang="en">
<head>
<meta charset="utf-8">
<title>Varenne Estate Agents – Letterhead</title>
<link href="https://fonts.googleapis.com/css2?family=Questrial&display=swap" rel="stylesheet">
<style>
  :root {
    --plum: #4c1038;
    --orange: #f15a24;
    --orange-light: #f6956a;
    --navy: #1d3a6e;
    --ink: #3a3a3a;
    --paper: #ffffff;
    --backdrop: #ececec;
  }
  * { margin: 0; padding: 0; box-sizing: border-box; }
  html, body { width: 982px; height: 1200px; overflow: hidden; background: var(--backdrop); }
  body { font-family: "Questrial", "Century Gothic", sans-serif; }
  .letterhead {
    position: relative;
    width: 982px;
    height: 1200px;
    background: var(--paper);
    overflow: hidden;
  }
  .header-wave { position: absolute; top: 0; left: 0; width: 982px; height: 290px; display: block; }
  .brand { position: absolute; left: 96px; top: 58px; display: flex; align-items: center; gap: 38px; }
  .brand-mark { width: 108px; height: 108px; border-radius: 50%; background: var(--orange); }
  .brand-text { display: flex; flex-direction: column; gap: 14px; }
  .brand-name { color: #fff; font-size: 38px; letter-spacing: 7px; line-height: 1; }
  .brand-tagline { color: var(--orange); font-size: 15px; letter-spacing: 5.5px; line-height: 1; }
  .company-details {
    position: absolute; right: 51px; top: 56px;
    text-align: right; color: #fff; font-size: 16px; line-height: 24px;
  }
  .company-reg { color: var(--orange); letter-spacing: 1.5px; margin-top: 8px; }
  .letter-body { position: absolute; left: 48px; right: 51px; top: 320px; bottom: 140px; }
  .footer-contacts {
    position: absolute; left: 46px; top: 1138px;
    display: flex; gap: 14px; color: var(--ink); font-size: 15.5px; align-items: center;
  }
  .contact { display: flex; align-items: center; gap: 5px; }
  .contact svg { width: 17px; height: 17px; }
  .accreditations { position: absolute; left: 653px; top: 1084px; display: flex; align-items: center; gap: 26px; }
  .badge-pelv { width: 72px; height: 72px; border-radius: 50%; background: var(--navy); }
  .badge-adjudicator { width: 187px; height: 62px; background: var(--navy); border-radius: 2px; }
</style>
</head>
<body>
<div class="letterhead">
  <svg class="header-wave" viewBox="0 0 982 290" aria-hidden="true">
    <defs>
      <linearGradient id="ribbon" x1="0" x2="1" y1="0" y2="0">
        <stop offset="0" stop-color="var(--orange-light)"/>
        <stop offset="0.35" stop-color="var(--orange)"/>
        <stop offset="1" stop-color="var(--orange)"/>
      </linearGradient>
    </defs>
    <path d="M0,82 C80,225 200,283 330,277 C480,270 620,172 800,166 C880,163 950,176 982,192 V0 H0 Z" fill="url(#ribbon)"/>
    <path d="M0,80 C90,205 210,255 330,254 C480,252 620,166 800,160 C880,157 940,165 982,176 V0 H0 Z" fill="var(--plum)"/>
  </svg>

  <div class="brand">
    <div class="brand-mark"></div>
    <div class="brand-text">
      <div class="brand-name">VARENNE</div>
      <div class="brand-tagline">ESTATE AGENTS</div>
    </div>
  </div>

  <div class="company-details">
    <p>VARENNE LTD, 412A Harwood Lane</p>
    <p>London NW8 2QT</p>
    <p class="company-reg">Reg No: 07734519</p>
  </div>

  <main class="letter-body"></main>

  <footer>
    <div class="footer-contacts">
      <span class="contact">
        <svg viewBox="0 0 20 20"><circle cx="10" cy="10" r="8.5" fill="none" stroke="var(--orange)" stroke-width="1.6"/><path d="M7 5.5 l2 2.5 -1.2 1.2 c.8 1.6 1.7 2.5 3.2 3.2 l1.2-1.2 2.5 2 -1.2 1.8 c-3.5-.3-6.8-3.6-7.2-7.4z" fill="var(--orange)"/></svg>
        020 7946 0321
      </span>
      <span class="contact">
        <svg viewBox="0 0 20 20"><rect x="2" y="6" width="16" height="11" rx="1.5" fill="var(--orange)"/><path d="M2.5 7 L10 12.5 L17.5 7" fill="none" stroke="#fff" stroke-width="1.4"/></svg>
        info@varenne.co.uk
      </span>
      <span class="contact">
        <svg viewBox="0 0 20 20" fill="none" stroke="var(--orange)" stroke-width="1.5"><circle cx="10" cy="10" r="8"/><ellipse cx="10" cy="10" rx="3.5" ry="8"/><path d="M2 10h16M3.5 6h13M3.5 14h13"/></svg>
        www.varenne.co.uk
      </span>
    </div>
    <div class="accreditations">
      <div class="badge-pelv" role="img" aria-label="PELV licensed member badge"></div>
      <div class="badge-adjudicator" role="img" aria-label="Homestead Adjudicator membership badge"></div>
    </div>
  </footer>
</div>
</body>
</html>
```